KVR Biz Cards

We are a property management company that manages luxury level residential estates. As such, we need a business card design that gives a high end feel. The idea at the moment is to list the services offered on the back of the card, and our company information on the front of the card.

Services for the back of the card are as follows:
Professional Property Management service, Home Hosting & Concierge Service, Holliday Home / Income Property Management

```html
<!DOCTYPE html>
<html lang="en">
<head>
<meta charset="utf-8">
<title>KVR Business Cards</title>
<link rel="stylesheet" href="https://fonts.googleapis.com/css2?family=Montserrat:wght@400;500;600;700&display=swap">
<style>
  :root {
    --page: #ffffff;
    --ink: #000000;
    --paper: #ffffff;
    --bronze: #8e5f31;
    --light: #ffffff;
    --edge: #2a2a2a;
  }
  * { margin: 0; padding: 0; box-sizing: border-box; }
  html, body {
    width: 1200px; height: 1000px; overflow: hidden;
    background: var(--page);
    font-family: "Montserrat", Arial, sans-serif;
  }
  .canvas { position: relative; width: 1200px; height: 1000px; }
  .card {
    position: absolute; left: 203px; width: 795px; height: 455px;
    border: 1px solid var(--edge); overflow: hidden;
  }
  .card--back { top: 22px; }
  .card--front { top: 523px; }
  .card__top { position: absolute; left: 0; top: 0; width: 100%; }
  .card__band { position: absolute; left: 0; bottom: 0; width: 100%; background: var(--bronze); color: var(--light); }
  .card--back .card__top { height: 281px; background: var(--ink); }
  .card--back .card__band { height: 173px; }
  .card--front .card__top { height: 282px; background: var(--paper); }
  .card--front .card__band { height: 172px; }

  .brand { position: absolute; display: flex; flex-direction: column; align-items: center; }
  .brand__name { font-size: 29px; font-weight: 700; line-height: 1; letter-spacing: 0.4px; }
  .brand__tagline { font-size: 18.5px; font-weight: 500; line-height: 1; margin-top: 4px; }

  .card--back .brand { right: 35px; top: 189px; }
  .card--back .brand__name, .card--back .brand__tagline { color: var(--light); }

  .card--front .brand { left: 0; width: 100%; top: 197px; }
  .card--front .brand__name { color: var(--ink); }
  .card--front .brand__tagline { color: var(--bronze); }

  .services { position: absolute; left: 33px; top: 34px; }
  .services__title { font-size: 24px; font-weight: 700; margin-bottom: 10px; }
  .services__list { list-style: none; font-size: 19px; line-height: 23px; }

  .contact__name { position: absolute; top: 31px; width: 100%; text-align: center; font-size: 25px; font-weight: 700; }
  .contact__grid { position: absolute; top: 83px; font-size: 19px; line-height: 30px; }
  .contact__grid--left { left: 56px; }
  .contact__grid--right { left: 379px; }
</style>
</head>
<body>
<main class="canvas">
  <section class="card card--back">
    <div class="card__top">
      <div class="brand">
        <div class="brand__name">KEVRAN MANAGEMENT</div>
        <div class="brand__tagline">Engineered to Give You Peace of Mind</div>
      </div>
    </div>
    <div class="card__band">
      <div class="services">
        <h2 class="services__title">SERVICES</h2>
        <ul class="services__list">
          <li>Professional Property Management service</li>
          <li>Home Hosting &amp; Concierge Service</li>
          <li>Holliday Home / Income Property Management</li>
        </ul>
      </div>
    </div>
  </section>

  <section class="card card--front">
    <div class="card__top">
      <div class="brand">
        <div class="brand__name">KEVRAN MANAGEMENT</div>
        <div class="brand__tagline">Engineered to Give You Peace of Mind</div>
      </div>
    </div>
    <div class="card__band">
      <div class="contact__name">Daniel Reeve (CEO)</div>
      <div class="contact__grid contact__grid--left">
        <p>w: kevranmanagement.com</p>
        <p>p: +012-555-0147</p>
      </div>
      <div class="contact__grid contact__grid--right">
        <p>e: hello@kevranmanagement.com</p>
        <p>a: 45 Example Row, Anywhere, London</p>
      </div>
    </div>
  </section>
</main>
</body>
</html>
```